Brontaro Web Site

Redesigned web site for Brontaro Ltd (www.brontaro-example.co.uk). This is to feature new logo (attached). Brontaro Ltd is a company which specialises in Geographic Information Systems and Geographic data - we call ourselves GIS Data Specialists. We are looking for something which conveys our professionalism and our experience. There will be more pages than on the current Brontaro website. There will be: Home, Data Migration, Data Cleansing & Validation, Data Analysis, Data Maintenance, Data Quality and an About Us page. All these should be accessible from each page on the website.
Updates
I didn't really think to say that the content of the web site is going to change from the current one we have. There will be more pages than on the current one. They will be: Home, Data Migration, Data Cleansing & Validation, Data Analysis, Data Maintenance, Data Quality and an About Us page. All these should be accessible from each page on the website. I didn't really think through the fact that the number of pages / areas to access can influence the layout of the site, sorry.
Target Market(s)
Utility Companies (e.g. telecommunications providers, energy companies), local government.
Industry/Entity Type
It Company
Look and feel

```html
<!DOCTYPE html>
<html lang="en">
<head>
<meta charset="utf-8">
<title>Brontaro – GIS Data Specialists</title>
<link href="https://fonts.googleapis.com/css2?family=Open+Sans:wght@400;600&family=Cinzel:wght@400&family=Oswald:wght@400&family=Nunito:wght@800&family=Noto+Serif:wght@700&family=PT+Sans:wght@400;700&display=swap" rel="stylesheet">
<style>
:root{
  --teal:#9dd7dd;
  --teal-dark:#2aa5a8;
  --teal-line:#7ccfd3;
  --red:#b0232a;
  --green:#6a9f2a;
  --grey-text:#777;
  --body-text:#333;
  --light:#efefef;
  --white:#fff;
}
*{margin:0;padding:0;box-sizing:border-box}
html,body{width:1200px;height:1097px;overflow:hidden;background:var(--white);font-family:"PT Sans",sans-serif;color:var(--body-text)}
.canvas{position:relative;width:1200px;height:1097px}
.abs{position:absolute}
.top-band{left:0;top:10px;width:1200px;height:180px;background:var(--teal)}
.page{left:100px;top:10px;width:1000px;height:1002px;background:var(--white)}
.logo-mark{left:135px;top:40px;width:60px;height:100px;border-radius:50%;background:var(--teal);opacity:.75}
.logo-name{left:203px;top:68px;font-family:"Open Sans",sans-serif;font-weight:600;font-size:40px;color:var(--grey-text);letter-spacing:.5px;line-height:1}
.logo-tag{left:206px;top:114px;font-family:"Open Sans",sans-serif;font-size:18px;color:#8a8a8a;line-height:1}
.utility-links{right:133px;top:39px;font-size:13px;color:#888;word-spacing:4px}
.utility-links span{margin:0 8px;color:#aaa}
.care-box{left:750px;top:69px;width:318px;height:92px;background:var(--teal)}
.care-key{left:768px;top:45px;width:100px;height:110px;border-radius:14px;background:linear-gradient(145deg,#fff,#d9d9d9);transform:rotate(12deg)}
.care-text{left:870px;top:76px;width:200px;text-align:center;font-family:"Nunito",sans-serif;font-weight:800;font-size:16px;color:#111;line-height:27px}
.care-text .phone{color:var(--red);font-size:20px}
.nav-shadow{left:140px;top:190px;width:900px;height:6px;background:radial-gradient(ellipse at top,rgba(0,0,0,.12),transparent 70%)}
.main-nav{left:117px;top:211px;font-size:12.5px;color:var(--teal-dark);text-transform:uppercase;white-space:nowrap}
.main-nav a{color:inherit;text-decoration:none}
.main-nav i{font-style:normal;color:#999;margin:0 8px}
.search{left:911px;top:206px;width:140px;height:23px;border:1px solid #bbb;font-size:11px;color:#aaa;padding:4px 7px}
.search-go{left:1060px;top:206px;width:23px;height:23px;border:1px solid #bbb;font-size:12px;color:#888;text-align:center;line-height:20px}
.nav-rule{left:100px;top:240px;width:1000px;border-top:1px dotted var(--teal-line)}
.hero{left:99px;top:243px;width:1002px;height:326px;border:1px solid var(--teal-line);background:linear-gradient(90deg,#fff 0%,#f3f3f3 60%,#fff 100%)}
.hero-art{left:140px;top:290px;width:310px;height:210px;background:radial-gradient(ellipse at 55% 45%,#e6e6e6,#fbfbfb 70%);border-radius:12px}
.hero-title{left:533px;top:315px;font-family:"Cinzel",serif;font-size:25px;color:#222;letter-spacing:.5px}
.hero-copy{left:534px;top:366px;width:508px;font-size:11px;line-height:18px;color:#888;text-align:justify}
.hero-more{left:535px;top:448px;font-weight:700;font-size:14px;color:var(--red);display:flex;align-items:center;gap:6px}
.card{width:300px;height:212px}
.card-body{left:0;top:62px;width:300px;height:150px;background:linear-gradient(90deg,#eee,#fff 85%)}
.card-fold{left:0;top:194px;width:0;height:0;border-top:18px solid #bbb;border-right:18px solid transparent}
.card-icon{left:14px;top:3px;width:48px;height:48px}
.card-title{left:75px;top:8px;font-family:"Oswald",sans-serif;font-size:19px;line-height:20px;text-transform:uppercase}
.card-title .first{color:var(--green);display:block}
.card-title .second{color:var(--red);display:block}
.card-list{left:14px;top:72px;width:270px;list-style:none;font-size:11px;line-height:20px}
.card-list li{position:relative;padding-left:20px;margin-bottom:9px}
.card-list li::before{content:"";position:absolute;left:2px;top:4px;width:10px;height:12px;border-radius:50% 50% 50% 0;background:var(--green)}
.card-more{left:213px;top:198px;width:88px;height:20px;background:var(--red);color:var(--white);font-size:11px;text-align:center;line-height:20px;box-shadow:0 2px 3px rgba(0,0,0,.3)}
.footer{left:100px;top:853px;width:1000px;height:135px;background:var(--light)}
.footer-mark{left:129px;top:868px;width:30px;height:54px;border-radius:50%;background:var(--teal);opacity:.7}
.footer-name{left:164px;top:882px;font-family:"Open Sans",sans-serif;font-weight:600;font-size:23px;color:#999;line-height:1}
.footer-sub{left:166px;top:907px;font-family:"Open Sans",sans-serif;font-size:10px;color:#aaa}
.footer-tag{left:129px;top:933px;font-family:"Noto Serif",serif;font-weight:700;font-size:15.5px;line-height:20px;color:var(--teal)}
.footer-rule{left:404px;top:868px;width:1px;height:108px;background:#ddd}
.footer-col{top:880px;font-size:12px;line-height:30px;color:#666}
.footer-col a{display:block;color:inherit;text-decoration:underline}
.bottom-band{left:0;top:1012px;width:1200px;height:85px;background:var(--teal)}
.copyright{left:103px;top:1033px;font-size:12px;color:#333}
.social{top:1033px;height:25px;background:#2f5b8f}
</style>
</head>
<body>
<div class="canvas">
  <div class="abs top-band"></div>
  <div class="abs page"></div>

  <header>
    <div class="abs logo-mark"></div>
    <div class="abs logo-name">Brontaro</div>
    <div class="abs logo-tag">GIS Data Specialists</div>
    <div class="abs utility-links">Login<span>|</span>Register<span>|</span>Contact</div>
    <div class="abs care-box"></div>
    <div class="abs care-key" role="img" aria-label="Keyboard key with help symbol"></div>
    <div class="abs care-text">24/7 Customer Care<br>Call @<br><span class="phone">1800 5550192</span></div>
  </header>

  <div class="abs nav-shadow"></div>
  <nav class="abs main-nav">
    <a href="#">Home</a><i>•</i><a href="#">About Brontaro</a><i>•</i><a href="#">Data Consultancy</a><i>•</i><a href="#">Software Development</a><i>•</i><a href="#">Software Products</a><i>•</i><a href="#">Contact Us</a>
  </nav>
  <div class="abs search">Search Text Here..</div>
  <div class="abs search-go">go</div>
  <div class="abs nav-rule"></div>

  <section>
    <div class="abs hero"></div>
    <div class="abs hero-art" role="img" aria-label="White puzzle pieces with a green dollar sign on the last piece"></div>
    <h1 class="abs hero-title">GIS DATA SPECIALISTS</h1>
    <p class="abs hero-copy">We provide a vast bank of knowledge and experience to offer an all encompassing service. This ensures that you, as a customer, reap the maximum benefits from your data and systems through utilising a combination of our skilled consultants, analysts and developers that will work with you and your requirements to help achieve your business objectives.</p>
    <div class="abs hero-more">
      <svg width="21" height="21" viewBox="0 0 21 21"><circle cx="10.5" cy="10.5" r="10" fill="#5aa02c"/><path d="M10.5 5v11M5 10.5h11" stroke="#fff" stroke-width="3"/></svg>
      Read More
    </div>
  </section>

  <section class="abs card" style="left:116px;top:600px">
    <div class="abs card-body"></div>
    <div class="abs card-fold"></div>
    <div class="abs card-icon" role="img" aria-label="Globe icon" style="border-radius:50%;background:radial-gradient(circle at 35% 35%,#8fd3ff,#1e6fc4)"></div>
    <h2 class="abs card-title"><span class="first">Data</span><span class="second">Consultancy</span></h2>
    <ul class="abs card-list">
      <li>We can help in the collation and organisation of that information.</li>
      <li>We can help with the maintenance of the data.</li>
      <li>We can help leverage additional information from the data.</li>
    </ul>
    <div class="abs card-more">Read More &gt;&gt;</div>
  </section>

  <section class="abs card" style="left:459px;top:600px">
    <div class="abs card-body"></div>
    <div class="abs card-fold"></div>
    <div class="abs card-icon" role="img" aria-label="Computer monitor icon" style="background:linear-gradient(135deg,#6aa6ff,#0a2fb8);border:3px solid #ccc;height:40px;top:8px"></div>
    <h2 class="abs card-title"><span class="first">Software</span><span class="second">Development</span></h2>
    <ul class="abs card-list">
      <li>We make it our business to understand our client's needs.</li>
      <li>Carefully customised software.</li>
      <li>Partners with Norvale Grid Systems, Cartiva, Draftwell, Terrabyte and Kestrel.</li>
    </ul>
    <div class="abs card-more">Read More &gt;&gt;</div>
  </section>

  <section class="abs card" style="left:801px;top:600px">
    <div class="abs card-body"></div>
    <div class="abs card-fold"></div>
    <div class="abs card-icon" role="img" aria-label="Software box and disc icon" style="background:linear-gradient(135deg,#d6ecff,#5c9fd6);border-radius:4px;width:40px"></div>
    <h2 class="abs card-title" style="left:68px"><span class="first">Software</span><span class="second">Products</span></h2>
    <ul class="abs card-list">
      <li>Our GeoLens product allows geographic information to be viewed and queried.</li>
      <li>Data Cleansing and Transformation.</li>
      <li>Our DataPort product allows data to be extracted from or imported to a GIS.</li>
    </ul>
    <div class="abs card-more" style="left:191px">Read More &gt;&gt;</div>
  </section>

  <footer>
    <div class="abs footer"></div>
    <div class="abs footer-mark"></div>
    <div class="abs footer-name">Brontaro</div>
    <div class="abs footer-sub">GIS Data Specialists</div>
    <div class="abs footer-tag">Geographic Information<br>Systems and Geographic Data</div>
    <div class="abs footer-rule"></div>
    <div class="abs footer-col" style="left:431px"><a href="#">Brontaro</a><a href="#">Data Consultancy</a><a href="#">Software Development</a></div>
    <div class="abs footer-col" style="left:587px"><a href="#">Software Products</a><a href="#">Asset Management</a><a href="#">Electricity, Power, Mining</a></div>
    <div class="abs footer-col" style="left:756px"><a href="#">Entertainment &amp; Media</a><a href="#">Government</a><a href="#">Retail &amp; Consumer</a></div>
    <div class="abs footer-col" style="left:923px"><a href="#">Pharmaceuticals</a><a href="#">Automotive</a><a href="#">Banking &amp; Capital Markets</a></div>

    <div class="abs bottom-band"></div>
    <p class="abs copyright">Copyright Notice © 2009 brontaro-example.co.uk. All rights reserved.</p>
    <div class="abs social" style="left:904px;width:33px"></div>
    <div class="abs social" style="left:941px;width:62px;background:#333"></div>
    <div class="abs social" style="left:1009px;width:25px;background:#5fb8e6"></div>
    <div class="abs social" style="left:1038px;width:25px;background:#1f76b5"></div>
    <div class="abs social" style="left:1068px;width:25px;background:#2b63c8"></div>
  </footer>
</div>
</body>
</html>
```